Need a new office flyer

I would like an 8.5 x 11" flyer made that can be emailed or printed out and handed to potential customers.  The flyer should include our existing logo and continuity of branding.   I am a commercial real estate broker and market myself to business with 5-50 employee's that are looking to buy or lease space to run their business from.  I focus my efforts on office & warehouse space. The flyer should have a banner "need a new location "
"VLD commercial real estate specializes in helping business and professionals buy/sell or lease  the best spaces for their business.  Take the stress & time out of finding the best location for your business and negotiating a great deal  VLD will do it for you and the best part our service is free to you. Working with VLD is easy as 1, 2, 3
1. Call, Text, Email us today and let us know what your looking to do.
2. VLD  will prepare a list of all the best available spaces that meet your specifications and set up tours of your favorites.
3. We will negotiate the best terms for your space. and help you with all the  details of getting your new space ready for you.
Don't forget the that our services are free to Buyers and Tenants so don't waste your companies time searching for locations, we already know where they are!
Contact us today!
Dale Norcutt
DRE 07354128
VLD Commercial Real Estate
555-317-4829
d.norcutt@vldprop-example.com

```html
<!DOCTYPE html>
<html lang="en">
<head>
<meta charset="utf-8">
<title>VLD Commercial Real Estate – Need a New Location</title>
<link href="https://fonts.googleapis.com/css2?family=Titillium+Web:wght@300;400;600;700;900&display=swap" rel="stylesheet">
<style>
  :root {
    --brand-blue: #2b6ea4;
    --ink: #2a2a2a;
    --grey-mark: #c9c9c9;
    --page-bg: #d4d4d4;
    --sheet: #ffffff;
    --panel-fade: #efefef;
    --card-line: #2b6ea4;
  }
  * { box-sizing: border-box; margin: 0; padding: 0; }
  html, body { width: 1200px; height: 1128px; overflow: hidden; }
  body {
    background: var(--page-bg);
    font-family: "Titillium Web", sans-serif;
    color: var(--ink);
    position: relative;
  }
  .flyer {
    position: absolute; left: 160px; top: 2px;
    width: 880px; height: 1124px;
    background: linear-gradient(to bottom, var(--sheet) 0, var(--sheet) 835px, var(--panel-fade) 900px, var(--sheet) 1040px);
    overflow: hidden;
  }
  .abs { position: absolute; }

  .brand { left: 47px; top: 45px; display: flex; align-items: center; gap: 12px; }
  .brand-dot { width: 104px; height: 104px; border-radius: 50%; border: 5px solid var(--brand-blue); }
  .brand-name { font-weight: 900; font-size: 72px; line-height: 1; color: var(--brand-blue); letter-spacing: 3px; }

  .hero-art {
    left: 428px; top: 44px; width: 452px; height: 316px;
    background: linear-gradient(160deg, #ffffff 0%, #e9ecef 35%, #cfe3c6 60%, #e3e0da 80%, #ffffff 100%);
    border-radius: 4px;
  }
  .watermark-ring {
    left: 520px; top: 20px; width: 470px; height: 470px; border-radius: 50%;
    border: 18px solid #f2f2f2;
  }

  .headline { left: 48px; font-weight: 700; line-height: 1; letter-spacing: -2px; }
  .headline-need { top: 172px; font-size: 118px; color: var(--ink); }
  .headline-box { left: 47px; top: 278px; width: 364px; height: 96px; background: var(--brand-blue); }
  .headline-new { top: 266px; left: 58px; font-size: 118px; color: #fff; }
  .headline-location { top: 366px; left: 52px; font-size: 120px; color: var(--brand-blue); }

  .intro-marker { left: 55px; top: 495px; }
  .intro {
    left: 96px; top: 497px; width: 736px;
    font-size: 17.6px; line-height: 20.5px; text-align: justify; text-align-last: left;
  }

  .step {
    top: 655px; width: 248px; height: 184px;
    border: 1.5px solid var(--card-line); border-radius: 14px; background: #fff;
    box-shadow: 0 14px 12px -12px rgba(0,0,0,.18);
  }
  .step-1 { left: 48px; } .step-2 { left: 314px; } .step-3 { left: 581px; }
  .step-icon {
    position: absolute; left: 76px; top: -48px; width: 96px; height: 96px;
    border-radius: 50%; background: var(--brand-blue);
    display: flex; align-items: center; justify-content: center;
  }
  .step-text {
    position: absolute; left: 20px; right: 20px; top: 60px;
    font-size: 17.5px; line-height: 22px; text-align: center;
  }

  .reminder {
    left: 0; width: 880px; top: 876px; text-align: center;
    font-size: 20.5px; line-height: 27px; font-weight: 300;
  }
  .reminder strong { color: var(--brand-blue); font-weight: 600; }
  .tagline {
    left: 0; width: 880px; top: 935px; text-align: center;
    font-size: 33px; font-weight: 700; line-height: 1; letter-spacing: -.3px;
  }

  .contact-band {
    left: 0; top: 993px; width: 780px; height: 45px; background: var(--brand-blue);
    clip-path: polygon(24px 0, 100% 0, 100% 100%, 0 100%);
  }
  .contact-band-text {
    left: 34px; top: 994px; color: #fff; font-weight: 700; font-size: 26px; line-height: 42px;
  }
  .contact-band-rule { left: 562px; top: 1014px; width: 180px; height: 2px; background: #fff; }

  .badge {
    left: 744px; top: 980px; width: 136px; height: 136px; border-radius: 50%;
    background: #fff; border: 5px solid var(--brand-blue);
    box-shadow: 0 0 0 4px #fff, 0 0 0 7px #9a9a9a;
  }

  .agent { left: 31px; top: 1046px; }
  .agent-name { font-size: 25px; font-weight: 700; color: var(--brand-blue); line-height: 1; }
  .agent-license { font-size: 19px; font-weight: 600; line-height: 1.2; margin-top: 2px; }
  .phone-icon { left: 215px; top: 1052px; }
  .office { left: 255px; top: 1050px; }
  .office-name { font-size: 15px; font-weight: 400; line-height: 1; }
  .office-phone { font-size: 31px; font-weight: 700; color: var(--brand-blue); line-height: 1.1; }
  .divider { left: 478px; top: 1056px; width: 1px; height: 46px; background: #666; }
  .globe-icon { left: 490px; top: 1066px; }
  .links { left: 522px; top: 1056px; font-size: 13.5px; line-height: 21px; }
</style>
</head>
<body>
<main class="flyer">
  <div class="abs watermark-ring" aria-hidden="true"></div>
  <div class="abs hero-art" role="img" aria-label="Illustration of a hand placing a red location pin on a folded city map"></div>

  <div class="abs brand">
    <span class="brand-dot" aria-hidden="true"></span>
    <span class="brand-name">VLD</span>
  </div>

  <h1>
    <span class="abs headline headline-need">NEED</span>
    <span class="abs headline-box" aria-hidden="true"></span>
    <span class="abs headline headline-new">A NEW</span>
    <span class="abs headline headline-location">LOCATION</span>
  </h1>

  <svg class="abs intro-marker" width="26" height="76" viewBox="0 0 26 76" aria-hidden="true">
    <polygon points="0,0 26,38 0,76" fill="var(--grey-mark)"/>
  </svg>
  <p class="abs intro">VLD commercial real estate specializes in helping business and professionals buy/sell or lease the best spaces for their business. Take the stress &amp; time out of finding the best location for your business and negotiating a great deal VLD will do it for you and the best part our service is free to you. Working with VLD is easy as 1, 2, 3</p>

  <section class="abs step step-1">
    <div class="step-icon">
      <svg width="66" height="66" viewBox="0 0 66 66" fill="none" stroke="#fff" stroke-width="3">
        <circle cx="33" cy="33" r="29"/>
        <path d="M22 19c3-2 5-1 6 2l2 5c1 2 0 3-2 4l-1 1c1 4 5 8 9 9l1-1c1-2 2-3 4-2l5 2c3 1 4 3 2 6-2 3-5 4-9 3-9-3-16-10-19-19-1-4 0-7 2-10z" fill="#fff" stroke="none"/>
      </svg>
    </div>
    <p class="step-text">Call, Text, Email us today and let us know what your looking to do</p>
  </section>

  <section class="abs step step-2">
    <div class="step-icon">
      <svg width="62" height="62" viewBox="0 0 62 62" fill="none" stroke="#fff" stroke-width="2.5" stroke-linecap="round">
        <rect x="10" y="6" width="34" height="50" rx="3"/>
        <path d="M15 17l2 2 4-4M15 28l2 2 4-4M15 39l2 2 4-4M15 50l2 2 4-4"/>
        <path d="M25 17h14M25 28h14M25 39h14M25 50h14"/>
        <path d="M50 16v34l2 4 2-4V16z"/>
      </svg>
    </div>
    <p class="step-text">VLD will prepare a list of all the best available spaces that meet your specifications and set up tours of your favorites.</p>
  </section>

  <section class="abs step step-3">
    <div class="step-icon">
      <svg width="70" height="70" viewBox="0 0 70 70" fill="none" stroke="#fff" stroke-width="2.5" stroke-linejoin="round" stroke-linecap="round">
        <path d="M4 26l10-10 8 8-10 10zM66 26L56 16l-8 8 10 10z"/>
        <path d="M22 24l8-4c3-1 5-1 7 1l10 9"/>
        <path d="M48 24l-10 0-8 7c-2 2 0 5 3 4l7-4"/>
        <path d="M12 34l14 14c2 2 5 2 6 0l2-2M18 40l8 8M24 36l10 10c2 2 4 2 6 0l8-8 10-4"/>
      </svg>
    </div>
    <p class="step-text">We will negotiate the best terms for your space. and help you with all the details of getting your new space ready for you.</p>
  </section>

  <p class="abs reminder">Don't forget the that <strong>our services are free to Buyers and Tenants so<br>don't waste your companies time searching for locations</strong></p>
  <p class="abs tagline">WE ALREADY KNOW WHERE THEY ARE!</p>

  <div class="abs contact-band" aria-hidden="true"></div>
  <p class="abs contact-band-text">FOR MORE DETAILS, CONTACT US TODAY!</p>
  <div class="abs contact-band-rule" aria-hidden="true"></div>
  <div class="abs badge" aria-hidden="true"></div>

  <div class="abs agent">
    <p class="agent-name">DALE NORCUTT</p>
    <p class="agent-license">DRE 07354128</p>
  </div>

  <svg class="abs phone-icon" width="26" height="46" viewBox="0 0 26 46" fill="none" stroke="#777" stroke-width="2.5" aria-hidden="true">
    <rect x="2" y="2" width="22" height="42" rx="3"/>
    <path d="M2 36h22M2 8h22"/>
  </svg>
  <div class="abs office">
    <p class="office-name">VLD COMMERCIAL REAL ESTATE</p>
    <p class="office-phone">555-317-4829</p>
  </div>

  <div class="abs divider" aria-hidden="true"></div>
  <svg class="abs globe-icon" width="26" height="26" viewBox="0 0 26 26" fill="none" stroke="#777" stroke-width="1.8" aria-hidden="true">
    <circle cx="13" cy="13" r="11"/>
    <ellipse cx="13" cy="13" rx="5" ry="11"/>
    <path d="M2 13h22M4 7h18M4 19h18"/>
  </svg>
  <div class="abs links">
    <p>d.norcutt@vldprop-example.com</p>
    <p>www.vldprop-example.com</p>
  </div>
</main>
</body>
</html>
```